Business Card Design for Event Planning Company

Create a business card for event planning company using our new logo. After I pick the design, I will need files made for 6 employees. Our company provides event design & logistics services as well as venue management. The font should be sans serif and complementary to the logo. I will need to know the name of the font selected for the final design. The phone numbers listed should be separated by "." not "-"

Address for the card
PO Box 318, Washington, DC 20019

Card One
Lorna Pettibone
lpettibone@galavoyant.com
202.481.7730

Card Two
Miriam Okonkwo
mokonkwo@galavoyant.com
202.556.2047

Card Three
Tessa Varnholt
tvarnholt@galavoyant.com
978.620.4471

Card Four
Robin Fess
rfess@galavoyant.com
202.718.3362

Card Five
Ada-Rose Pelletan-Uzor
adarose@galavoyant.com
202.839.1205

Card Six
Beatrix Holloway
Beatrix@galavoyant.com
202.492.6618

Target Market(s)

Corporate/Non-Profit

Industry/Entity Type

Event Planning

Contact Information for Business Card

Address for the card

Card One
Lorna Pettibone
lpettibone@galavoyant.com
202.481.7730

Card Two
Miriam Okonkwo
202.556.2047

Card Three
Tessa Varnholt
978.620.4471

Card Four
Robin Fess
rfess@galavoyant.com
202.718.3362

Card Five
Ada-Rose Pelletan-Uzor
202.839.1205

Card Six
Beatrix Holloway
202.492.6618

Font styles to use
Sans Serif

Colors

Designer to choose colors to be used in the design.

Requirements
Must have
• Two-sided with logo
Should not have
• Extra colors or be too busy

```html
<!DOCTYPE html>
<html lang="en">
<head>
<meta charset="utf-8">
<title>Gala Voyant – Business Card</title>
<link rel="stylesheet" href="https://fonts.googleapis.com/css2?family=Open+Sans:wght@300;400;600;700&display=swap">
<style>
  :root {
    --backdrop: #e9e9e9;
    --card-dark: #231f20;
    --card-light: #f2f2f2;
    --teal: #5ba7a5;
    --ink: #231f20;
    --text-light: #f4f4f4;
  }
  html, body {
    margin: 0;
    padding: 0;
    width: 1200px;
    height: 900px;
    overflow: hidden;
    background: var(--backdrop);
    font-family: "Open Sans", Arial, sans-serif;
  }
  .canvas {
    position: relative;
    width: 1200px;
    height: 900px;
  }
  .card {
    position: absolute;
    box-shadow: 0 4px 14px rgba(0,0,0,0.18);
    overflow: hidden;
  }

  /* Front */
  .card-front {
    left: 78px;
    top: 34px;
    width: 588px;
    height: 364px;
    background: var(--card-dark);
    color: var(--text-light);
  }
  .holder-name {
    position: absolute;
    left: 38px;
    top: 52px;
    margin: 0;
    font-size: 22px;
    font-weight: 700;
    letter-spacing: 0.3px;
    color: var(--teal);
    text-transform: uppercase;
  }
  .address {
    position: absolute;
    left: 38px;
    top: 201px;
    margin: 0;
    font-size: 15.5px;
    line-height: 22px;
    font-style: normal;
  }
  .contact-list {
    position: absolute;
    left: 38px;
    top: 264px;
    margin: 0;
    padding: 0;
    list-style: none;
    font-size: 15.5px;
    line-height: 21.5px;
  }
  .contact-list li {
    display: flex;
    align-items: center;
    gap: 7px;
  }
  .contact-icon {
    width: 12px;
    height: 12px;
    fill: var(--teal);
    flex: none;
  }
  .brand-panel {
    position: absolute;
    right: 0;
    top: 0;
    width: 276px;
    height: 364px;
    background: var(--teal);
  }

  /* Back */
  .card-back {
    left: 388px;
    top: 505px;
    width: 567px;
    height: 352px;
    background: var(--card-light);
    color: var(--ink);
  }
  .wordmark {
    position: absolute;
    left: 0;
    right: 0;
    top: 170px;
    margin: 0;
    text-align: center;
    font-size: 46px;
    font-weight: 300;
    letter-spacing: 0.5px;
    color: var(--teal);
  }
  .web-address {
    position: absolute;
    left: 0;
    right: 0;
    top: 300px;
    margin: 0;
    text-align: center;
    font-size: 15px;
    font-weight: 600;
    color: var(--ink);
  }
  .web-address .domain { color: var(--teal); }
</style>
</head>
<body>
<main class="canvas">
  <section class="card card-front" aria-label="Business card front">
    <h1 class="holder-name">Lorna Pettibone</h1>
    <address class="address">PO Box 318,<br>Washington, DC 20019</address>
    <ul class="contact-list">
      <li>
        <svg class="contact-icon" viewBox="0 0 24 24" aria-hidden="true"><path d="M6.6 10.8a15.2 15.2 0 0 0 6.6 6.6l2.2-2.2a1 1 0 0 1 1-.25 11.4 11.4 0 0 0 3.6.57 1 1 0 0 1 1 1V20a1 1 0 0 1-1 1A17 17 0 0 1 3 4a1 1 0 0 1 1-1h3.5a1 1 0 0 1 1 1c0 1.25.2 2.45.57 3.57a1 1 0 0 1-.25 1z"/></svg>
        202.481.7730
      </li>
      <li>
        <svg class="contact-icon" viewBox="0 0 24 24" aria-hidden="true"><path d="M2 5h20v14H2z M2 5l10 7 10-7" /><path d="M2 5h20L12 12z" fill="#231f20"/></svg>
        lpettibone@galavoyant.com
      </li>
      <li>
        <svg class="contact-icon" viewBox="0 0 24 24" aria-hidden="true"><circle cx="12" cy="12" r="10"/><path d="M7 8c2 0 3 1 3 3s2 2 2 4-1 3 0 5M15 4c0 2 1 3 3 3s3 1 4 2" stroke="#231f20" stroke-width="1.6" fill="none"/></svg>
        www.galavoyant.com
      </li>
    </ul>
    <div class="brand-panel" role="img" aria-label="Large decorative brand symbol in white on teal"></div>
  </section>

  <section class="card card-back" aria-label="Business card back">
    <p class="wordmark">galavoyant</p>
    <p class="web-address">www.<span class="domain">galavoyant</span>.com</p>
  </section>
</main>
</body>
</html>
```